HIgh-end jewelry designer needs a business card design

I need a business card design for the ecclectic & rather expensive jewelry designs. My approach to my work is to combine very old jewelry offset with contemporary items. I enjoy the idea of legacy as well as repurposing finely crafted items that are not possible to create any longer. My desire is to celebrate the past in a contemporary & funky way. The name of my business is MERIVALE. I see my business card design as simple & yet enigmatic as possible. In the end... clean, simple & understated is the look I am after. Thank you for your consideration...

Target Market(s)

I will use this business card for the trade as well as customers

Industry/Entity Type

Business

Contact Information for Business Card

Corinne Halvard Owner/Designer 555-274-8163

Requirements
Must have
• Clean & simple sophisticated design using the word "Merivalle" as the logo. I like the idea of a play on the word itself, perhaps even using different fonts (i.e.: a bold helvetica combined with a lovely script). I'm afraid to say more because I don't want to limit creative input. Gosh, sometimes it's ok to break the rules!
Nice to have
• In my mind, I have imagined this business card to be simple, using my company name "Merivale" in a playful yet sophisticated manner. I believe that doing something beautifully simple can be a true challenge. I have imagined something with just black & white, however I am open to ideas... after all that's why I'm here!
Should not have
• As Mozart once said... "It has too many notes!" I know I'm being silly, but I don't want it to be complicated or overly ornate.

```html
<!DOCTYPE html>
<html lang="en">
<head>
<meta charset="utf-8">
<title>Merivale — Business Card</title>
<link rel="stylesheet" href="https://fonts.googleapis.com/css2?family=Inter:wght@300;400&display=swap">
<style>
  :root {
    --backdrop: #efefef;
    --card-front: #4f2e46;
    --card-back: #ffffff;
    --logo-ink: #d8cad5;
    --contact-ink: #4f2e46;
    --card-edge: #e2e2e2;
  }
  * { margin: 0; padding: 0; box-sizing: border-box; }
  html, body {
    width: 1200px;
    height: 900px;
    overflow: hidden;
    background: var(--backdrop);
  }
  .stage {
    position: relative;
    width: 1200px;
    height: 900px;
  }
  .card {
    position: absolute;
    left: 343px;
    width: 510px;
    height: 284px;
    border-radius: 38px;
  }
  .card--front {
    top: 137px;
    background: var(--card-front);
    display: flex;
    align-items: center;
    justify-content: center;
  }
  .card--back {
    top: 438px;
    background: var(--card-back);
    border: 1px solid var(--card-edge);
  }
  .wordmark {
    font-family: "Inter", Helvetica, Arial, sans-serif;
    font-weight: 300;
    font-size: 37px;
    letter-spacing: 0.36em;
    margin-right: -0.36em;
    color: var(--logo-ink);
  }
  .contact-line {
    position: absolute;
    left: 0;
    right: 0;
    bottom: 32px;
    text-align: center;
    font-family: "Inter", Helvetica, Arial, sans-serif;
    font-weight: 400;
    font-size: 16px;
    letter-spacing: 0.02em;
    color: var(--contact-ink);
  }
</style>
</head>
<body>
  <main class="stage">
    <section class="card card--front" aria-label="Card front">
      <h1 class="wordmark">MERIVALE</h1>
    </section>
    <section class="card card--back" aria-label="Card back">
      <p class="contact-line">Corinne Halvard Owner/Designer 555-274-8163</p>
    </section>
  </main>
</body>
</html>
```